Ridgeway Framers Business Card

I'm looking for a business card design for a start-up Handyman/Construction Company. The organization will double as a ministry to the homeless, hoping to create job opportunity and training to the homeless, providing a pathway back to being "homed". I'm looking for a simple to "seeming" simple design. Open to all thoughts.

Industry/Entity Type

Ministry

Requirements
Must have
• Logo (Attached), Name, Phone, Email and Address. Note - "*Registered and Insured".

```html
<!DOCTYPE html>
<html lang="en">
<head>
<meta charset="utf-8">
<title>Ridgeway Framers Business Card</title>
<link href="https://fonts.googleapis.com/css2?family=Open+Sans:wght@400;700;800&display=swap" rel="stylesheet">
<style>
  :root {
    --backdrop: #3d3a3b;
    --card: #e3dfd9;
    --ink: #2f3450;
    --accent: #6a3f8a;
    --text: #2b2b2b;
  }
  * { margin: 0; padding: 0; box-sizing: border-box; }
  html, body { width: 1200px; height: 588px; overflow: hidden; background: var(--backdrop); }
  body { position: relative; font-family: "Open Sans", Arial, sans-serif; }
  .card {
    position: absolute; top: 186px; width: 393px; height: 225px;
    background: var(--card); border-radius: 9px;
  }
  .card--front { left: 158px; }
  .card--back { left: 660px; }

  .wordmark {
    position: absolute; color: var(--ink); font-weight: 800;
    text-transform: uppercase; line-height: 1; white-space: nowrap;
  }
  .card--front .wordmark { right: 28px; top: 22px; font-size: 22px; letter-spacing: 0.5px; }
  .card--back .wordmark { left: 78px; top: 92px; font-size: 27px; letter-spacing: 0.5px; }

  .tagline {
    position: absolute; left: 80px; top: 72px; color: var(--ink);
    font-size: 7px; font-weight: 700; letter-spacing: 2.2px; text-transform: uppercase;
  }

  .identity {
    position: absolute; left: 41px; top: 146px; width: 253px;
    padding-bottom: 3px; border-bottom: 1px solid var(--text);
    font-size: 11.5px; color: var(--text); letter-spacing: 0.4px; white-space: nowrap;
  }
  .identity .person { font-weight: 800; }
  .identity .role { font-weight: 400; }

  .contact { position: absolute; font-size: 10px; color: var(--text); list-style: none; }
  .contact li { display: flex; align-items: center; height: 14.5px; white-space: nowrap; }
  .contact svg { width: 8px; height: 8px; margin-right: 7px; fill: var(--text); flex: none; }
  .contact--address { left: 26px; top: 165px; }
  .contact--phones { left: 26px; top: 181px; }
  .contact--web { left: 154px; top: 181px; }
</style>
</head>
<body>
  <section class="card card--front">
    <div class="wordmark">Ridgeway Framers</div>
    <div class="identity"><span class="person">DANA WHITFIELD</span> | <span class="role">CHIEF EXECUTIVE OFFICER</span></div>
    <ul class="contact contact--address">
      <li><svg viewBox="0 0 10 10"><path d="M5 0a3.5 3.5 0 0 0-3.5 3.5C1.5 6 5 10 5 10s3.5-4 3.5-6.5A3.5 3.5 0 0 0 5 0zm0 5a1.5 1.5 0 1 1 0-3 1.5 1.5 0 0 1 0 3z"/></svg>4820 Millbrook Avenue, Albany, NY 12203</li>
    </ul>
    <ul class="contact contact--phones">
      <li><svg viewBox="0 0 10 10"><path d="M1 3c0-1 1-2 4-2s4 1 4 2v1H7V3H3v1H1zM2 5h6l1 4H1z"/></svg>703-555-0148</li>
      <li><svg viewBox="0 0 10 10"><path d="M3 0h4a1 1 0 0 1 1 1v8a1 1 0 0 1-1 1H3a1 1 0 0 1-1-1V1a1 1 0 0 1 1-1zm0 1.5v6h4v-6z"/></svg>301-555-0172</li>
    </ul>
    <ul class="contact contact--web">
      <li><svg viewBox="0 0 10 10"><path d="M0 2h10v6H0zm1 1v.4l4 2.4 4-2.4V3z"/></svg>info@ridgewayframers.com</li>
      <li><svg viewBox="0 0 10 10"><path d="M5 0a5 5 0 1 0 0 10A5 5 0 0 0 5 0zm0 1.2c.7 0 1.4 1.5 1.5 3.3h-3C3.6 2.7 4.3 1.2 5 1.2zM3.5 5.5h3C6.4 7.3 5.7 8.8 5 8.8S3.6 7.3 3.5 5.5z"/></svg>www.ridgewayframers.com</li>
    </ul>
  </section>

  <section class="card card--back">
    <div class="tagline">Registered and Insured</div>
    <div class="wordmark">Ridgeway Framers</div>
  </section>
</body>
</html>
```